Baby Adoption Announcement

I'm looking for a simple, understated and modern baby adoption announcement.

The baby is a boy, but I don't want anything that is blue or particularly boyish. No storks, baby baskets, rattles, or traditional baby announcement designs. No cutesy or busy designs.

Should measure 5.25 x 8.25 inches to fit in an A9 envelope.

Simple graphics MIGHT include birds, grasses, trees, rivers. I'm open to other ideas. Text can be a single color or multi colored. Graphics are not mandatory.

Since this is text heavy, I'd like the designer to be REALLY GOOD at choosing fonts and typesetting.

Text should read:

Memory answers us bright on your face—
Impossibly, we spoke and were silent
Together before all of this. (in italics)

Cornelius Tobias Pelter Quist
Born on March 16, 2012 in Boston, MA
and entrusted to us by his birthmother, Gwenda.

Named Cornelius, which means God is with us, after Gwenda’s grandfather &
Tobias, after Toby and St. Tobias of Karvel

• Should measure 5.25 x 8.25 inches to fit in A9 envelope.

• The baby is a boy, but I don't want anything that is blue or particularly boyish. No storks, baby baskets, rattles, or traditional baby announcement designs. Nothing cutesy or busy.

```html
<!DOCTYPE html>
<html lang="en">
<head>
<meta charset="utf-8">
<title>Cornelius Tobias Pelter Quist – Adoption Announcement</title>
<link href="https://fonts.googleapis.com/css2?family=Source+Sans+3:ital,wght@0,400;0,700;1,400&display=swap" rel="stylesheet">
<style>
  :root {
    --ink: #4a2a06;
    --lime-center: #f2fd26;
    --lime-mid: #e2f820;
    --lime-edge: #7cce1c;
    --sky-glow: rgba(255, 255, 255, 0.55);
  }
  * { margin: 0; padding: 0; box-sizing: border-box; }
  html, body {
    width: 882px;
    height: 1200px;
    overflow: hidden;
    background: #ffffff;
  }
  .announcement {
    position: relative;
    width: 882px;
    height: 1200px;
    background: radial-gradient(ellipse 75% 62% at 50% 52%,
      var(--lime-center) 0%, var(--lime-mid) 55%, var(--lime-edge) 100%);
    color: var(--ink);
    font-family: "Source Sans 3", sans-serif;
    text-align: center;
  }
  .sky-art {
    position: absolute;
    left: 50px;
    top: 30px;
    width: 800px;
    height: 190px;
    border-radius: 60px;
    background: radial-gradient(ellipse 60% 55% at 50% 50%,
      var(--sky-glow) 0%, rgba(255, 255, 255, 0) 100%);
  }
  .verse {
    position: absolute;
    top: 346px;
    left: 0;
    width: 100%;
    font-style: italic;
    font-size: 32px;
    line-height: 43px;
  }
  .details {
    position: absolute;
    top: 636px;
    left: 0;
    width: 100%;
  }
  .child-name {
    font-weight: 700;
    font-size: 33px;
    line-height: 44px;
    margin-bottom: 2px;
  }
  .details p {
    font-size: 26px;
    line-height: 40px;
  }
  .naming {
    margin-top: 30px;
  }
</style>
</head>
<body>
  <main class="announcement">
    <div class="sky-art" role="img" aria-label="Simple white clouds drifting across the top of the card with a white sun at the upper right"></div>

    <section class="verse">
      <p>Memory answers us bright on your face</p>
      <p>Impossibly, we spoke and were silent</p>
      <p>Together before all of this.</p>
    </section>

    <section class="details">
      <h1 class="child-name">Cornelius Tobias Pelter Quist</h1>
      <p>Born on March 16, 2012 in Boston, MA</p>
      <p>and entrusted to us by his first mother, Gwenda,</p>
      <p>who named him</p>

      <div class="naming">
        <p>Cornelius, which means "God is with us,"</p>
        <p>after his Ugandan great-grandfather</p>
        <p>and</p>
        <p>Tobias, which means "Victory of the people,"</p>
        <p>after Toby and St. Tobias of Karvel</p>
      </div>
    </section>
  </main>
</body>
</html>
```